Brochure Design Project

Color brochure with text, graphics, and photos. (I will provide the text). 4 pages of 8 1/2 X 11". This is a brochure about dental implants.
Attached is the text and logo for the brochure.

See new parameters and information on the brochure project.

Included in the brochure is our address: Brookfield Dental Care, 218 Larchmont Avenue, Brookfield, PA 17342.  717-482-6915.  www.brookfielddentalcare-example.com.

Martin R. Pulaski, D.M.D., M.A.G.D., F.I.C.O.I. (Attached is photo for brochure)file://localhost/Users/mrpdmd7/Pictures/iPhoto%20Library/Masters/2003/Office%20Pictures/Dr.%20Pulaski%202.jpg

Target Market(s)

Adults, primarily senior adults.

Industry/Entity Type

Dental

```html
<!DOCTYPE html>
<html lang="en">
<head>
<meta charset="utf-8">
<title>Dental Implants – Questions and Answers</title>
<link rel="stylesheet" href="https://fonts.googleapis.com/css2?family=Source+Sans+3:wght@400;500;600&display=swap">
<style>
  :root {
    --teal: #72bcc7;
    --navy: #2f5597;
    --ink: #1d1d1d;
    --label: #4aa3c9;
    --footer-ink: #1f3566;
  }
  * { margin: 0; padding: 0; box-sizing: border-box; }
  html, body { width: 926px; height: 1200px; overflow: hidden; background: #fff; }
  body { font-family: "Source Sans 3", "Helvetica Neue", Arial, sans-serif; color: var(--ink); }
  .page { position: relative; width: 926px; height: 1200px; overflow: hidden; background: #fff; }
  .top-band { position: absolute; left: 0; top: 0; width: 100%; height: 55px; background: var(--teal); }
  .top-rule { position: absolute; left: 0; top: 55px; width: 100%; height: 12px; background: var(--navy); }
  .bottom-rule { position: absolute; left: 0; top: 1127px; width: 100%; height: 9px; background: var(--navy); }
  .bottom-band { position: absolute; left: 0; top: 1136px; width: 100%; height: 64px; background: var(--teal); }
  .content {
    position: absolute; left: 39px; right: 20px; top: 97px;
    font-size: 17px; line-height: 22.3px; text-align: justify;
  }
  .content p { margin-bottom: 22.3px; }
  .content p.tight { margin-bottom: 0; }
  .num { display: inline-block; width: 59px; font-weight: 500; }
  .lead { font-weight: 500; }
  .q, .a { color: var(--label); font-weight: 500; }
  .indent { text-indent: 59px; }
  .footer {
    position: absolute; left: 28px; right: 30px; top: 1150px;
    display: flex; align-items: center;
    font-size: 13px; color: var(--footer-ink);
  }
  .footer .address { width: 420px; }
  .footer .sep { font-weight: 600; font-size: 18px; width: 30px; }
  .footer .web { width: 240px; }
  .footer b { font-weight: 600; }
</style>
</head>
<body>
<div class="page">
  <div class="top-band"></div>
  <div class="top-rule"></div>

  <main class="content">
    <p><span class="num">10.</span><span class="lead">Eliminate denture adhesives FOREVER!</span> There is no need for messy denture adhesives because implants are attached to the bone.</p>

    <p class="tight"><span class="num">11.</span><span class="lead">Missing teeth replaced with implants will not affect your other teeth.</span> Replacing missing teeth with implant supported crowns and bridges does not compromise or damage the adjacent natural, healthy teeth as other methods do.</p>
    <p class="tight">For example, when you wear a partial denture, you have clamps that hook onto adjacent teeth, which put pressure on them that causes them to loosen and come out.</p>
    <p>Bridges require grinding down the adjacent teeth so that the bridge can be cemented onto them. This tooth structure can never be replaced and the long-term health of these teeth are compromised.</p>

    <p><span class="q">Q:</span> Am I a Candidate for Implant Treatment?</p>
    <p><span class="a">A:</span> Many people are missing at least one tooth. Wanting good health and a beautiful, natural smile makes you a candidate for dental implant treatment. There are few medical conditions that can undermine the success of implant treatment, such as uncontrolled diabetes. Quality and quantity of available bone for implant placement is more often a factor in qualifying for dental implants than medical conditions. However, even people who have lost significant amount of bone can qualify for dental implant treatment with additional procedures. Advances in this type of treatment have made it possible for thousands of patients who would not previously have been considered candidates, to have successful implant procedures.</p>

    <p><span class="q">Q:</span> How Long Will it Take to Complete the Treatment?</p>
    <p class="tight"><span class="a">A:</span> You will notice a difference almost immediately. However, the entire process can take several months to complete. This depends on the type, and quantity of implants you need, along with the quality of bone in which the implants are placed, as well as the type of replacement solution you choose.</p>
    <p class="indent">There are treatment options that are faster, such as dentures; however, none of these traditional methods prevent bone loss, or give the type of natural look and feel like implants do.</p>

    <p><span class="q">Q:</span> Will I need to have One Implant Placed for each Tooth that is Missing?</p>
    <p><span class="a">A:</span> No. In fact, it is possible to replace all of the lower teeth with an over denture that is supported by only 2-4 implants. On the other hand, sometimes it might work to your advantage to replace your back teeth with an implant for each tooth to provide additional strength.</p>

    <p><span class="q">Q:</span> How do I know If I’m To Old for Implants?</p>
    <p><span class="a">A:</span> Great question. Your overall health and your desire to improve the quality of life are much more important than your age. We currently have patients from 40 years old to 70+ years old. There have been reports of people who are in their 90’s who have had implants placed with no problems.</p>

    <p><span class="q">Q:</span> How Long Do Implants Last?</p>
    <p><span class="a">A:</span> Research has shown that implants have been successful for over 30 years. However, our goal is to make them so they last a lifetime. This is a great improvement over dentures, which have a life expectancy of 5 years, and/or bridges where the expected lifespan of 7-10 years.</p>
  </main>

  <div class="bottom-rule"></div>
  <div class="bottom-band"></div>
  <footer class="footer">
    <span class="address">Brookfield Dental Care, 218 Larchmont Avenue, Brookfield, PA 17342</span>
    <span class="sep">|</span>
    <span class="web">www.brookfielddentalcare-example.com</span>
    <span class="sep">|</span>
    <span><b>phone</b> 717-482-6915</span>
  </footer>
</div>
</body>
</html>
```